Norwegian Mobile Home/Cabin Producer Needs Brochure Design

We make and deliver our own brand of mobile homes especially made for Norway and it's weather conditions. We differ from other brands in building quality in regards to a much more solid construction, insulation and choices. We work with our customer from the beginning and build them after their demands and wishes.
We need a brochure that holds us out as top of the line. We deliver mobile homes of all kinds and sizes. Both to the private and professional sector.
For the professional sector, mainly camping sites we want to show, lodges-, sanitary- and kitchen wagoons etc.
So we need a brochure of 14-20 pages in A4 where the double pages can be printed in A3 format.
We have logo (provided). But we need cover as well as back suggestions.
It should start with pages where we can teel who we are and stand for.Piicture(s) and space for some editable text (which we can write in norwegian). The text part can have a transparent background......or not. Give us your best shot. Also a smaller part in the private sector that shows winter time.
We want other pages for the private sector that shows what we deliver and the possibilities of choices.
Pages for the the professional sector.
Pages that show our production. How we transport. And the split construction. Only pictures from this portfolio here. (see fotoskap portfolios)
Take a look at provided pictures and our website www.solvikhytta.no for inspiration.
Here's a FotoSkap link to Pictures to choose from. http://bildelagr.example/K4TQ9P
(Hope it Works, let me know if not)
Our company name in small letters "fjordgrønn hyttebygg" means directly translated "fjordgreen cabin builds".
Looking forward to your suggestions.
Target Market(s)
Private market for vacation mobile homes. Camping sites and similar
Industry/Entity Type
Insulation
Requirements
Must have
- Our logo on the front page. Simple but inviting and professional
Logo and address on the back.

```html
<!DOCTYPE html>
<html lang="no">
<head>
<meta charset="utf-8">
<title>fjordgrønn hyttebygg – brosjyreside</title>
<link rel="stylesheet" href="https://fonts.googleapis.com/css2?family=Anton&family=Cabin:wght@400;600&display=swap">
<style>
  :root {
    --paper: #ffffff;
    --masthead-green: #bee385;
    --masthead-letter: #e6f6d8;
    --sky-rule: #9fd3ee;
    --initial-tan: #d2b7a1;
    --body-ink: #2a2a2a;
    --forest-dark: #3f6a2c;
    --forest-light: #9fd07a;
  }
  * { margin: 0; padding: 0; box-sizing: border-box; }
  html, body { width: 900px; height: 1200px; overflow: hidden; background: var(--paper); }
  .page {
    position: relative;
    width: 900px;
    height: 1200px;
    overflow: hidden;
    background: var(--paper);
  }
  .masthead {
    position: absolute;
    left: 0; top: 0;
    width: 885px; height: 232px;
    background: var(--masthead-green);
    overflow: hidden;
  }
  .masthead__name {
    position: absolute;
    left: 50px; top: -18px;
    font-family: "Cabin", sans-serif;
    font-weight: 400;
    font-size: 214px;
    line-height: 1;
    letter-spacing: 2px;
    white-space: nowrap;
    color: var(--masthead-letter);
  }
  .sky-rule {
    position: absolute;
    left: 14px; top: 232px;
    width: 876px; height: 6px;
    background: var(--sky-rule);
  }
  .spread-edge {
    position: absolute;
    right: 0; top: 0;
    width: 15px; height: 1200px;
    background: linear-gradient(180deg, #c9d7b8 0%, #7fa85a 30%, #8a6e52 60%, #b7c79e 85%, #e2e6da 100%);
  }
  .drop-initial {
    position: absolute;
    left: 0; top: 280px;
    width: 540px; height: 400px;
  }
  .drop-initial text {
    font-family: "Anton", sans-serif;
    fill: var(--initial-tan);
  }
  .intro-text {
    position: absolute;
    left: 537px; top: 294px;
    width: 248px;
    font-family: "Cabin", sans-serif;
    font-size: 15.2px;
    line-height: 20.75px;
    color: var(--body-ink);
    text-align: justify;
    hyphens: auto;
    height: 398px;
    overflow: hidden;
  }
  .cabin-photo {
    position: absolute;
    left: 208px; top: 750px;
    width: 486px; height: 317px;
    background: linear-gradient(180deg, var(--forest-light) 0%, #6fa44c 40%, #2d3440 62%, #a99a8a 85%, #c8bfb5 100%);
  }
</style>
</head>
<body>
<main class="page">
  <header class="masthead">
    <h1 class="masthead__name">fjordgrønn hyttebygg</h1>
  </header>
  <div class="sky-rule"></div>

  <svg class="drop-initial" viewBox="0 0 540 400" aria-hidden="true">
    <text x="60" y="388" font-size="500" textLength="475" lengthAdjust="spacingAndGlyphs">W</text>
  </svg>

  <p class="intro-text" lang="la">Lorem ipsum dolor sit amet, consectetuer adipiscing elit. Nam nibh. Nunc varius facilisis eros. Sed erat. In in velit quis arcu ornare laoreet. Curabitur adipiscing luctus massa. Integer ut purus ac augue commodo commodo. Nunc nec mi eu justo tempor consectetuer. Etiam vitae nisl. In dignissim lacus ut ante. Cras elit lectus, bibendum a, adipiscing vitae, commodo et, dui. Ut tincidunt tortor. Donec nonummy, enim in lacinia pulvinar, velit tellus scelerisque augue, ac posuere libero urna eget neque. Cras ipsum. Vestibulum pretium, lectus nec venenatis volutpat, purus lectus ultrices risus, a condimentum risus mi et quam. Pellentesque habitant morbi tristique.</p>

  <div class="cabin-photo" role="img" aria-label="Photo of a dark wooden reception cabin with a thatched roof among tall forest trees, with a flagpole and a red-and-white barrier in front"></div>

  <div class="spread-edge" role="img" aria-label="Edge of the facing page photo showing trees"></div>
</main>
</body>
</html>
```